Velitor creating new logo and business card design

Velitor is a consulting and business contribution for professional digital and real estate. We are specializing in lead generation / prospect want to invest in real estate that we connect with wealth manager or promoters. We identify prospects on all France, we call them and we put them in touch with professional able to meet their need. We wish to highlight our logo through the creation of value we bring to our customers. We provide them with contacts we obtained with tact, hence the solgan: tact in contact ... The logo should be created with the name Velitor. Playing with the name. If possible, put the slogan with the name and logo

Target Market(s)

Digital Immobiler

Industry/Entity Type

Digital

Contact Information for Business Card

RECTO :
Carvel Tiruan
CEO/Fondateur
Tel : 06 52 19 83 07
mail : tiruan.carvel@postelia.fr
VELITOR
14 rue des Orpailleurs
92340 Brevanne
VERSO : juste le logo

Logo Text

Velitor, le flair du lien

Font styles to use
Sans Serif
Decorative

Colors
ec1f27
e34297
85cae6
fbed22
f37122
9bcb3b
6b449b

Requirements
Must have
• We wish to have a logo that reflects our position as an innovative company and digital. The logo must be fluid, colorful and futuristic. We wish to highlight our logo through the creation of value we bring to our customers. We bring the contacts we have achieved tactfully, hence the solgan: tact in contact ...
Nice to have
• We like the Pluvex logo, toravine ... can bring out effect with a profile or target such I leave you free rein to your immagination
Should not have
• Nothing to report

```html
<!DOCTYPE html>
<html lang="fr">
<head>
<meta charset="utf-8">
<title>Velitor – Carte de visite</title>
<link rel="stylesheet" href="https://fonts.googleapis.com/css2?family=Montserrat:wght@700&family=Questrial&display=swap">
<style>
  :root {
    --brand-blue: #1a6fae;
    --brand-blue-deep: #135d96;
    --brand-green: #9bcb3b;
    --accent-sky: #85cae6;
    --accent-orange: #f37122;
    --accent-pink: #e34297;
    --accent-violet: #6b449b;
    --paper: #ffffff;
    --stage: #e9e6e1;
    --ink-light: #ffffff;
  }
  * { margin: 0; padding: 0; box-sizing: border-box; }
  html, body {
    width: 1200px; height: 800px; overflow: hidden;
    background: var(--stage);
  }
  .sheet {
    position: relative; width: 1200px; height: 800px;
    display: flex; flex-direction: column; align-items: center; justify-content: center; gap: 44px;
  }
  .card {
    position: relative; width: 560px; height: 320px;
    border-radius: 14px; overflow: hidden;
    box-shadow: 0 6px 18px rgba(0,0,0,.18);
    font-family: "Questrial", sans-serif;
  }
  .card-bg { position: absolute; inset: 0; width: 100%; height: 100%; }

  /* Recto */
  .contact-block { position: absolute; left: 42px; top: 78px; color: var(--ink-light); }
  .contact-name {
    font-family: "Montserrat", sans-serif; font-weight: 700;
    font-size: 19px; letter-spacing: .5px; line-height: 1.2;
  }
  .contact-role { font-size: 15px; margin-top: 2px; }
  .contact-lines { list-style: none; margin-top: 20px; }
  .contact-lines li {
    display: flex; align-items: center; gap: 10px;
    font-size: 15px; line-height: 23px; white-space: nowrap;
  }
  .contact-icon { width: 17px; height: 17px; flex: none; }
  .contact-address { font-size: 15px; line-height: 23px; margin-top: 20px; margin-left: 4px; }

  .brand { position: absolute; text-align: left; }
  .brand-name {
    font-family: "Questrial", sans-serif; color: var(--brand-green);
    font-size: 40px; letter-spacing: 1px; line-height: 1;
  }
  .brand-tagline { font-size: 12px; letter-spacing: .6px; margin-top: 6px; }
  .card-front .brand { left: 372px; top: 148px; }
  .card-front .brand-tagline { color: var(--brand-blue); }

  /* Verso */
  .card-back { background: var(--brand-blue); }
  .card-back .brand { left: 100px; top: 176px; }
  .card-back .brand-name { font-size: 44px; }
  .card-back .brand-tagline { color: var(--ink-light); font-size: 13px; }
</style>
</head>
<body>
<main class="sheet">

  <section class="card card-front" aria-label="Recto de la carte">
    <svg class="card-bg" viewBox="0 0 560 320" preserveAspectRatio="none" aria-hidden="true">
      <defs>
        <radialGradient id="blueGlow" cx="30%" cy="40%" r="70%">
          <stop offset="0" stop-color="#2a82c4"/>
          <stop offset="1" stop-color="#135d96"/>
        </radialGradient>
        <linearGradient id="accentBand" x1="0" y1="0" x2="0" y2="1">
          <stop offset="0" stop-color="#85cae6"/>
          <stop offset=".45" stop-color="#9bcb3b"/>
          <stop offset="1" stop-color="#9bcb3b"/>
        </linearGradient>
      </defs>
      <rect width="560" height="320" fill="url(#blueGlow)"/>
      <path d="M306 0 C234 62 238 250 358 320 L560 320 L560 0 Z" fill="url(#accentBand)"/>
      <path d="M322 0 C252 62 264 242 382 320 L560 320 L560 0 Z" fill="#ffffff"/>
    </svg>

    <div class="contact-block">
      <h1 class="contact-name">CARVEL TIRUAN</h1>
      <p class="contact-role">CEO / Fondateur</p>
      <ul class="contact-lines">
        <li>
          <svg class="contact-icon" viewBox="0 0 16 16" aria-hidden="true">
            <rect width="16" height="16" rx="3" fill="#9bcb3b"/>
            <path d="M5 3.5 L6.8 5.6 L5.9 6.8 C6.6 8.2 7.7 9.4 9.2 10.1 L10.4 9.2 L12.5 11 L11.6 12.5 C7.6 12.2 3.9 8.5 3.5 4.4 Z" fill="#fff"/>
          </svg>
          <span>06 52 19 83 07</span>
        </li>
        <li>
          <svg class="contact-icon" viewBox="0 0 16 16" aria-hidden="true">
            <rect width="16" height="16" rx="3" fill="#f37122"/>
            <rect x="3" y="4.5" width="10" height="7" fill="none" stroke="#fff" stroke-width="1.2"/>
            <path d="M3 4.8 L8 8.6 L13 4.8" fill="none" stroke="#fff" stroke-width="1.2"/>
          </svg>
          <span>tiruan.carvel@postelia.fr</span>
        </li>
        <li>
          <svg class="contact-icon" viewBox="0 0 16 16" aria-hidden="true">
            <rect width="16" height="16" rx="3" fill="#e34297"/>
            <circle cx="8" cy="8" r="4.6" fill="none" stroke="#fff" stroke-width="1.1"/>
            <ellipse cx="8" cy="8" rx="2" ry="4.6" fill="none" stroke="#fff" stroke-width="1"/>
            <path d="M3.4 8 H12.6" stroke="#fff" stroke-width="1"/>
          </svg>
          <span>www.velitor.fr</span>
        </li>
      </ul>
      <p class="contact-address">14 rue des Orpailleurs<br>92340 Brevanne</p>
    </div>

    <div class="brand">
      <p class="brand-name">VELITOR</p>
      <p class="brand-tagline">LE FLAIR DU LIEN</p>
    </div>
  </section>

  <section class="card card-back" aria-label="Verso de la carte">
    <div class="brand">
      <p class="brand-name">VELITOR</p>
      <p class="brand-tagline">LE FLAIR DU LIEN</p>
    </div>
  </section>

</main>
</body>
</html>
```